Coinvale Landing Page | A free, personalized stock market email

We are looking for someone to revamp our landing page at https://coinvale-example.com . You should get to know the product and what it offers, and present new designs for our landing page. Feel free to use assets that currently exist on the page, as well as any new assets that you can put together. This landing page should make it obvious what the product does and aim to dramatically increase our conversion rate. We are looking for creativity, uniqueness, and clarity of purpose.

Target Market(s)

People who are invested in, or interested in being invested in, the stock market

Industry/Entity Type

Finance

Number of Pages Required

1 page

Font styles to use
Sans Serif

Requirements
Must have
• Creativity, sleek/minimal design, existing color palette and logos
Nice to have
• Effective copy
Should not have
• Clutter

```html
<!DOCTYPE html>
<html lang="en">
<head>
<meta charset="utf-8">
<title>Coinvale — Do less. Know more.</title>
<link rel="stylesheet" href="https://fonts.googleapis.com/css2?family=Montserrat:wght@500;600;700&family=Open+Sans:wght@400;600&display=swap">
<style>
:root{
  --blue:#0c6db3;
  --blue-deep:#0867b0;
  --cyan:#00e6e8;
  --teal:#1aa6c8;
  --ink:#222;
  --body:#333;
  --grey-band:#f3f3f3;
  --blob:#e6f5fa;
  --white:#fff;
}
*{margin:0;padding:0;box-sizing:border-box}
html,body{width:1200px;height:4167px;overflow:hidden}
body{position:relative;background:var(--white);font-family:"Open Sans",sans-serif;color:var(--body)}
.abs{position:absolute}
.heading{font-family:"Montserrat",sans-serif;font-weight:600;color:var(--ink)}
.btn{position:absolute;display:flex;align-items:center;justify-content:center;border-radius:30px;
  background:linear-gradient(90deg,#12a9cf,var(--blue));color:var(--white);font-family:"Montserrat",sans-serif;
  font-weight:700;font-size:15px;letter-spacing:.3px;text-decoration:none}
.logo{display:flex;align-items:center;gap:10px;font-family:"Montserrat",sans-serif;font-weight:600;color:var(--blue)}
.logo .dot{border-radius:50%;background:var(--blue)}
.card-frame{position:absolute;background:var(--white);border-radius:18px;box-shadow:0 4px 18px rgba(0,0,0,.12);overflow:hidden}
.art{position:absolute;border-radius:12px}
.copy{font-size:19px;line-height:34px;color:var(--body)}

/* hero stock card */
.stock{position:absolute;left:691px;top:127px;width:276px;height:455px;background:var(--white);
  box-shadow:0 2px 12px rgba(0,0,0,.12);font-family:"Open Sans",sans-serif;color:var(--ink);padding:14px 10px}
.stock .tick{font-weight:600;color:var(--blue);font-size:16px}
.stock .price{display:inline-block;background:#e8eef3;border-radius:12px;padding:1px 8px;font-size:13px;font-weight:600;margin-left:6px}
.stock .small{font-size:9px;color:#555}
.stock .label{font-size:8px;color:#aab;letter-spacing:.4px;border-top:1px solid #eee;padding-top:10px;margin-top:12px}
.chg{display:inline-block;font-size:11px;font-weight:600;margin-right:14px}
.chg span{display:block;font-size:8px;font-weight:400;color:#555}

/* features */
.phone{position:absolute;top:2303px;width:98px;height:207px;border:4px solid #222;border-radius:12px;background:var(--white);padding:14px 8px;font-size:6px;color:#333}
.phone .bar{height:4px;background:#e4e4e4;margin:6px 0;border-radius:2px}
.phone .bar.g{background:#cdeccd;width:30%}
.feat-title{position:absolute;top:2536px;font-family:"Montserrat",sans-serif;font-weight:500;font-size:21px;color:var(--ink)}
.feat-copy{position:absolute;top:2592px;width:270px;font-size:15px;line-height:27px}

.footer{position:absolute;left:0;top:3722px;width:1200px;height:445px;background:var(--blue-deep);color:var(--white)}
.footer nav{position:absolute;top:214px;width:100%;display:flex;justify-content:center;gap:45px;font-size:17px}
.footer nav a{color:var(--white);text-decoration:none}
.social{position:absolute;top:297px;left:0;width:100%;display:flex;justify-content:center;gap:16px}
.social span{width:42px;height:42px;border:2px solid var(--white);border-radius:50%}
.legal{position:absolute;top:356px;width:100%;text-align:center;font-size:14px}
</style>
</head>
<body>

<!-- header -->
<div class="logo abs" style="left:97px;top:28px;font-size:40px"><span class="dot" style="width:36px;height:36px"></span>Coinvale</div>
<a class="btn" href="https://coinvale-example.com" style="left:980px;top:27px;width:122px;height:55px;font-size:14px">SIGN IN</a>

<!-- hero -->
<svg class="abs" style="left:598px;top:0" width="602" height="580" viewBox="0 0 602 580" aria-hidden="true">
  <path d="M60 0 H602 V330 C520 430 420 540 300 560 C160 585 20 480 2 310 C-10 180 20 60 60 0 Z" fill="var(--blob)"/>
</svg>
<h1 class="heading abs" style="left:95px;top:228px;font-size:70px;line-height:90px;font-weight:700">
  <span style="color:var(--blue)">Do less.</span><br>Know more.</h1>
<a class="btn" href="https://coinvale-example.com" style="left:99px;top:436px;width:199px;height:56px">SIGN UP FOR FREE</a>

<div class="stock">
  <div><span class="tick">SOLX</span><span class="price">$199.10</span></div>
  <div class="small" style="margin-top:4px">Solarix Energy, Inc.</div>
  <div style="margin-top:12px;padding-left:14px">
    <div class="chg" style="color:#111">+2.89%<span>1-Day</span></div>
    <div class="chg">−3.89%<span>30-Day</span></div>
    <div class="chg">+10.67%<span>1-Year</span></div>
  </div>
  <div class="label">ANALYST RATINGS</div>
  <div style="font-size:10px;margin:6px 0 0 6px">What <b>35</b> Wallstreet experts are saying:</div>
  <div style="display:flex;align-items:center;margin:14px 0 0 6px;gap:14px">
    <div style="width:48px;height:46px;background:#9ee0a6;border-radius:3px;font-size:10px;color:#2a7b37;display:flex;align-items:center;justify-content:center">BUY</div>
    <div style="width:96px"><div style="height:5px;background:#3ccf5c;border-radius:3px"></div><div style="height:5px;width:55%;background:#e2e6ea;margin-top:5px;border-radius:3px"></div><div style="height:5px;width:25%;background:#e2e6ea;margin-top:5px;border-radius:3px"></div></div>
    <div style="font-size:9px;line-height:12px">54.3% <b>Buy</b><br>31.4% Hold<br>14.3% Sell</div>
  </div>
  <div style="display:flex;align-items:center;gap:8px;margin:16px 0 0 12px;font-size:9px"><span style="width:18px;height:18px;border:2px solid var(--blue);border-radius:50%"></span><span>Target Price<br><b>$205</b></span></div>
  <div class="label">INDICATORS</div>
  <div style="margin:8px 8px 0;font-size:10px"><div style="display:flex;border-bottom:1px solid #ccc;font-weight:600;padding-bottom:3px"><span style="width:110px">Signal</span>Type</div>
  <div style="display:flex;padding:6px 0;border-bottom:1px solid #eee"><span style="width:110px">Moving Avg Cross</span>BUY</div></div>
  <div class="label">NEWS</div>
  <div style="margin:6px 6px 0;background:#eef1f4;border-radius:4px;padding:8px;display:flex;gap:8px">
    <div style="width:44px;height:40px;background:#c9b9a6;border-radius:3px" role="img" aria-label="News thumbnail"></div>
    <div style="font-size:10px;font-weight:600">Top 10 Solar Stocks To Watch This Year<div style="font-size:7px;font-weight:400;color:#777;margin-top:4px">By Dana Reyes via Tradeline</div></div>
  </div>
</div>

<!-- intro band -->
<section class="abs" style="left:0;top:679px;width:1200px;height:451px;background:var(--grey-band)">
  <h2 class="heading abs" style="left:97px;top:131px;font-size:39px;line-height:64px">Coinvale is your free,<br>personalized, data-<br>driven finance email</h2>
  <div class="art" role="img" aria-label="Illustration of a sloth in a suit waving, standing before a light blue drop shape" style="left:690px;top:56px;width:290px;height:370px;background:radial-gradient(ellipse at 50% 65%,#d7e8f2 0,#e5eef4 55%,var(--grey-band) 75%)"></div>
</section>

<!-- stop scanning -->
<div class="card-frame" style="left:97px;top:1248px;width:456px;height:366px">
  <div class="art" role="img" aria-label="Illustration of a sloth relaxing in a beach chair with a drink under the sun" style="inset:20px;background:linear-gradient(180deg,#fafafa,#eeeeee)"></div>
</div>
<h2 class="heading abs" style="left:647px;top:1292px;font-size:39px;line-height:64px">Stop scanning charts &amp;<br>chasing data</h2>
<p class="copy abs" style="left:647px;top:1451px;width:470px">Don't bend over backwards to get the investment insights you need. You have better ways to spend your time and energy.</p>

<!-- gradient band -->
<section class="abs" style="left:0;top:1735px;width:1200px;height:450px;background:linear-gradient(90deg,var(--cyan),var(--blue))">
  <h2 class="heading abs" style="left:97px;top:85px;font-size:39px;line-height:64px;color:var(--white)">Let the information come<br>right to you</h2>
  <p class="copy abs" style="left:97px;top:243px;width:460px;color:var(--white)">We'll send you curated market insights exactly when you want them.</p>
  <div class="art" role="img" aria-label="White line illustration of a sloth watching a winged envelope fly toward him" style="left:650px;top:85px;width:430px;height:310px;background:radial-gradient(ellipse at 40% 50%,rgba(255,255,255,.18),rgba(255,255,255,0) 70%)"></div>
</section>

<!-- features -->
<div class="phone" style="left:98px"><b style="font-size:7px">Your Schedule</b><div class="bar"></div><div class="bar"></div><div class="bar"></div><div class="bar g"></div><div class="bar"></div><div class="bar"></div><div class="bar"></div><div class="bar g"></div><div class="bar"></div><div class="bar"></div></div>
<div class="phone" style="left:471px"><b style="font-size:7px">Norvex Systems (NVSX)</b><div class="bar"></div><div class="bar g"></div><div class="bar"></div><div class="bar"></div><div class="bar g"></div><div class="bar"></div><div class="bar"></div><div class="bar"></div><div class="bar"></div></div>
<div class="phone" style="left:844px"><b style="font-size:7px">Daily Brief</b><div class="bar"></div><div class="bar"></div><div class="bar g" style="height:14px"></div><div class="bar"></div><div class="bar"></div><div class="bar"></div><div class="bar"></div><div class="bar"></div></div>

<h3 class="feat-title" style="left:98px">Your Schedule</h3>
<p class="feat-copy" style="left:97px">Customize when you get your email. Up to every half an hour during main exchange trading hours.</p>
<h3 class="feat-title" style="left:471px">Your Assets</h3>
<p class="feat-copy" style="left:470px">Choose from thousands of assets to include in your email. ORBT, KLNX, VRDA and more!</p>
<h3 class="feat-title" style="left:844px">All the Data</h3>
<p class="feat-copy" style="left:843px">We provide as much data on assets as we can, including price, price change, analyst ratings, technical indicators, and news. Want more? Let us know!</p>

<!-- stop paying -->
<section class="abs" style="left:0;top:2842px;width:1200px;height:488px;background:var(--grey-band)">
  <div class="card-frame" style="left:97px;top:60px;width:456px;height:366px">
    <div class="art" role="img" aria-label="Illustration of a sloth chasing floating stock tickers with a butterfly net in a grassy field" style="inset:20px;background:linear-gradient(180deg,#fbfbfb,#ececec)"></div>
  </div>
  <h2 class="heading abs" style="left:647px;top:100px;font-size:39px;line-height:64px">Stop paying for<br>information</h2>
  <p class="copy abs" style="left:647px;top:251px;width:470px">Don't spend a dime on financial information, use that money for investments</p>
  <p class="abs" style="left:647px;top:346px;font-family:'Montserrat',sans-serif;font-weight:600;font-size:19px;color:var(--teal)">Coinvale is free. Period.</p>
</section>

<!-- CTA -->
<h2 class="heading abs" style="left:0;top:3432px;width:1200px;text-align:center;font-size:54px;font-weight:600"><span style="color:var(--blue)">Do Less,</span> Know More Today</h2>
<a class="btn" href="https://coinvale-example.com" style="left:501px;top:3547px;width:198px;height:56px">SIGN UP FOR FREE</a>

<!-- footer -->
<footer class="footer">
  <div class="logo abs" style="left:0;width:1200px;justify-content:center;top:88px;font-size:66px;color:var(--white)"><span class="dot" style="width:60px;height:60px;background:var(--white)"></span>Coinvale</div>
  <nav><a href="#">ABOUT</a><a href="#">BLOG</a><a href="#">TERMS OF USE</a><a href="#">PRIVACY POLICY</a></nav>
  <div class="social"><span></span><span></span></div>
  <p class="legal">©Copyrights 2023 Coinvale &nbsp;&nbsp;| &nbsp;&nbsp;All Rights Reserved</p>
</footer>

</body>
</html>
```